Web Design for a company in Oil & Gas Business

We need a web design for our company based in Sydney called "Brindle Cove Exports". Main core of business are Engineering and Procurement services for Oil, Gas and Petrochemical Industry. It is important to highlight both capabilities in the website. Engineering services focuses on Technology Transfer, Know-how consultation as well as Detail Engineering. Regarding Procurement services, we provide full services starting from Offering, Order finalisation, Logistic coordination up to financial settlement of the project. Our Logo is combination of dark blue and Red. It is also important that the website would be compatible to various devices (mobile, tablet, PC).
Reason: I would like to receive more design ideas.

```html
<!DOCTYPE html>
<html lang="en">
<head>
<meta charset="utf-8">
<title>Brindle Cove Exports</title>
<link href="https://fonts.googleapis.com/css2?family=Ubuntu:wght@400;500&display=swap" rel="stylesheet">
<style>
  :root {
    --navy: #1c2f7a;
    --red: #c8262c;
    --ink: #222222;
    --muted: #555555;
    --nav-text: #3a3a3a;
    --caption-bg: rgba(40, 44, 58, 0.88);
    --vision-btn: #b8330f;
    --orange-btn: #e58a1c;
    --darkred-btn: #8f2a10;
    --footer-bg: #000000;
    --footer-text: #d8d8d8;
    --footer-muted: #8a8a8a;
    --bullet: #d4262c;
  }
  * { margin: 0; padding: 0; box-sizing: border-box; }
  html, body { width: 1200px; height: 948px; overflow: hidden; background: #ffffff; }
  body { font-family: "Ubuntu", Arial, sans-serif; color: var(--ink); }
  .page { position: relative; width: 1200px; height: 948px; overflow: hidden; }
  .abs { position: absolute; }

  /* header */
  .brand { left: 149px; top: 28px; display: flex; align-items: center; gap: 10px; white-space: nowrap; }
  .brand-dot { width: 44px; height: 44px; border-radius: 50%; background: var(--navy); flex: none; }
  .brand-name { font-size: 19px; font-weight: 500; color: var(--navy); letter-spacing: 0.2px; }
  .social { top: 55px; left: 878px; display: flex; gap: 16px; }
  .social span { width: 26px; height: 26px; border-radius: 50%; background: var(--navy); display: block; }
  .social span:nth-child(2), .social span:nth-child(3) { background: var(--red); }
  .main-nav { top: 104px; left: 0; width: 1200px; height: 24px; }
  .main-nav a { position: absolute; top: 0; font-family: Arial, sans-serif; font-size: 16px; color: var(--nav-text); text-decoration: none; white-space: nowrap; }

  /* hero */
  .hero { left: 0; top: 133px; width: 1200px; height: 374px;
    background: radial-gradient(ellipse at 45% 35%, #4a4a4c 0%, #2b2b2d 35%, transparent 60%),
                linear-gradient(90deg, #8e8e90 0%, #6d6d70 20%, #bfa88f 55%, #e3a05a 75%, #ee9332 100%); }
  .hero-caption { left: 152px; top: 296px; width: 487px; height: 136px; background: var(--caption-bg); }
  .hero-title { left: 185px; top: 316px; font-family: Arial, sans-serif; font-size: 22px; font-weight: normal; color: #ffffff; letter-spacing: 0.5px; white-space: nowrap; }
  .hero-text { left: 181px; top: 355px; width: 452px; font-size: 14.5px; line-height: 18px; color: #ffffff; }
  .btn { display: flex; align-items: center; justify-content: center; font-family: Arial, sans-serif; color: #ffffff; border-radius: 17px; text-decoration: none; white-space: nowrap; }
  .btn-vision { left: 472px; top: 415px; width: 143px; height: 32px; background: var(--vision-btn); font-size: 16px; }
  .hero-arrows { left: 999px; top: 463px; }

  /* news */
  .section-title { font-size: 29px; font-weight: 400; color: var(--ink); white-space: nowrap; }
  .news-title { left: 148px; top: 547px; }
  .news-thumb { left: 148px; top: 597px; width: 97px; height: 72px;
    background: linear-gradient(135deg, #6a3a1c 0%, #d98a2e 40%, #f2c66a 60%, #7a4a2a 100%); }
  .news-headline { left: 259px; top: 596px; width: 350px; font-size: 16px; font-weight: 500; line-height: 18px; color: var(--ink); }
  .news-body { left: 259px; top: 642px; width: 350px; font-size: 12.5px; line-height: 17px; color: var(--muted); }
  .btn-more { left: 259px; top: 728px; width: 108px; height: 33px; background: var(--orange-btn); font-size: 16px; }
  .btn-all { left: 376px; top: 728px; width: 95px; height: 33px; background: var(--darkred-btn); font-size: 16px; }

  /* projects */
  .projects-title { left: 692px; top: 548px; }
  .project-list { list-style: none; font-size: 12px; line-height: 16.7px; color: var(--ink); white-space: nowrap; }
  .project-list li { padding-left: 12px; position: relative; }
  .project-list li::before { content: ""; position: absolute; left: 0; top: 7px; width: 4px; height: 4px; border-radius: 50%; background: var(--bullet); }
  .projects-col-a { left: 694px; top: 596px; }
  .projects-col-b { left: 824px; top: 596px; }
  .help { left: 697px; top: 722px; display: flex; align-items: center; gap: 12px; white-space: nowrap; }
  .help-title { font-size: 29px; line-height: 30px; color: var(--ink); }
  .help-sub { font-size: 12px; color: var(--ink); margin-left: 4px; }

  /* footer */
  .footer { left: 0; top: 799px; width: 1200px; height: 149px; background: var(--footer-bg); }
  .footer-brand { left: 151px; top: 845px; display: flex; align-items: center; gap: 10px; white-space: nowrap; }
  .footer-brand .brand-dot { background: #ffffff; width: 38px; height: 38px; }
  .footer-brand .brand-name { color: #ffffff; font-size: 15px; }
  .copyright { left: 375px; top: 865px; font-family: Arial, sans-serif; font-size: 12px; line-height: 14px; color: var(--footer-muted); white-space: nowrap; }
  .footer-col h4 { font-family: Arial, sans-serif; font-size: 10.5px; font-weight: bold; color: #ffffff; margin-bottom: 3px; }
  .footer-col ul { list-style: none; margin-left: 10px; font-size: 10.5px; line-height: 14.7px; color: var(--footer-text); white-space: nowrap; }
  .col-software { left: 657px; top: 838px; }
  .col-contacts { left: 772px; top: 838px; }
  .col-resources { left: 939px; top: 838px; }
</style>
</head>
<body>
<div class="page">
  <header>
    <div class="abs brand"><span class="brand-dot"></span><span class="brand-name">Brindle Cove Exports</span></div>
    <div class="abs social" aria-label="Social links"><span></span><span></span><span></span><span></span></div>
    <nav class="abs main-nav">
      <a href="#" style="left:163px">About Us</a>
      <a href="#" style="left:288px">Expertise</a>
      <a href="#" style="left:404px">Knowledge</a>
      <a href="#" style="left:520px">Experience</a>
      <a href="#" style="left:643px">Projects</a>
      <a href="#" style="left:743px">Focus</a>
      <a href="#" style="left:837px">Contact</a>
      <a href="#" style="left:936px">Recruitment</a>
    </nav>
  </header>

  <section>
    <div class="abs hero" role="img" aria-label="Gloved hand holding lumps of coal"></div>
    <div class="abs hero-caption"></div>
    <h1 class="abs hero-title">BRINDLE COVE EXPORTS</h1>
    <p class="abs hero-text">I provide services to companies in the mining and oil and gas sector, to enabling them to plan and manage their construction projects more effectively.</p>
    <a href="#" class="abs btn btn-vision">Read Our Vision</a>
    <svg class="abs hero-arrows" width="44" height="26" viewBox="0 0 44 26">
      <polyline points="14,4 6,13 14,22" fill="none" stroke="#ffffff" stroke-width="3"/>
      <polyline points="30,4 38,13 30,22" fill="none" stroke="#ffffff" stroke-width="3"/>
    </svg>
  </section>

  <section>
    <h2 class="abs section-title news-title">Latest News</h2>
    <div class="abs news-thumb" role="img" aria-label="Close-up of industrial pipes"></div>
    <h3 class="abs news-headline">Exceed client’s expectations Act with integrity and honesty</h3>
    <p class="abs news-body">I have 20 years industry experience within engineering, construction, mining and the oil &amp; gas sector. I am well equipped to assist you and your company to deliver successful project outcomes..</p>
    <a href="#" class="abs btn btn-more">Read More</a>
    <a href="#" class="abs btn btn-all">All News</a>
  </section>

  <section>
    <h2 class="abs section-title projects-title">Projects</h2>
    <ul class="abs project-list projects-col-a">
      <li>Oil &amp; Gas</li><li>Iron Ore</li><li>Coal</li><li>Civil</li><li>Tenders</li><li>Telecomunications</li>
    </ul>
    <ul class="abs project-list projects-col-b">
      <li>New Industry</li><li>Petrochemical</li><li>Building And Constructionoil &amp; Gas</li><li>Engineering</li><li>Manufacturing</li><li>Rail</li>
    </ul>
    <div class="abs help">
      <svg width="44" height="44" viewBox="0 0 44 44" aria-hidden="true">
        <circle cx="22" cy="22" r="22" fill="#111111"/>
        <rect x="11" y="14" width="22" height="16" rx="2" fill="#ffffff"/>
        <polyline points="11,15 22,24 33,15" fill="none" stroke="#111111" stroke-width="2"/>
      </svg>
      <div>
        <div class="help-title">Need Help .</div>
        <div class="help-sub">Contact us now</div>
      </div>
    </div>
  </section>

  <footer>
    <div class="abs footer"></div>
    <div class="abs footer-brand"><span class="brand-dot"></span><span class="brand-name">Brindle Cove Exports</span></div>
    <p class="abs copyright">©2015 brindlecoveexports.com,<br>&nbsp;&nbsp;All right reserved</p>
    <div class="abs footer-col col-software"><h4>SOFTWARE</h4><ul><li>Advice</li><li>Vision</li><li>Solutions</li><li>Solutions</li><li>Perspective</li></ul></div>
    <div class="abs footer-col col-contacts"><h4>CONTACTS</h4><ul><li>Develop and evolve</li><li>Streamlines processes</li><li>Embrace and drive change</li><li>outcomes</li></ul></div>
    <div class="abs footer-col col-resources"><h4>RESOURCES</h4><ul><li>Systems</li><li>Standards</li><li>Procedures</li><li>Process</li></ul></div>
  </footer>
</div>
</body>
</html>
```